Kestrel Arc Services business card Design

I need a business card that will wow clients at first sight.

Kestrel Arc Services connects people with HOME & LIFESTYLE SERVICES, and the client pays the value that was created by our service, using. 'Settle On The Sum That Feels Fair".
Please look us up at www.kestrelarcservices.example to see our mission and services.

The new website is being launched in 8 weeks.

I need a business card to campaign LANDSCAPING however please design it to be easily modified to CLEANING SERVICE, PLUMBING Etc Etc.

Until our SEO campaign begins working I need business cards to leave with prospective clients for each individual service as appropriate.

Dorian Maltby
Creative Director
www.kestrelarcservices.example
1-888-517-4KAS
email: info@kestrelarcservices.example

Target Market(s)

Residential and commercial clients

Industry/Entity Type

Business

Contact Information for Business Card

2 sided

Font styles to use
Sans Serif

Requirements
Must have
• Im prefering a black card so far
• Logo
• "Settle On The Sum That Feels Fair" seal
• Complete Landscaping & Construction
• Tarnwell Services
• Contact details
• facebook kestrelarc services
• twitter @kestrelarc services
• Adaptable card easily to different services we offer at Kestrel Arc Services as per www.kestrelarcservices.example
Should not have
• Too much imagery

```html
<!DOCTYPE html>
<html lang="en">
<head>
<meta charset="utf-8">
<title>Kestrel Arc Services – Business Card</title>
<link rel="stylesheet" href="https://fonts.googleapis.com/css2?family=Open+Sans:wght@400;600&display=swap">
<style>
  :root {
    --backdrop: #e7e4df;
    --card: #252525;
    --text-light: #c9c9c9;
    --text-mid: #b5b5b5;
    --green: #7dc35b;
    --teal: #1f7f98;
    --blue: #2f5cb8;
    --purple: #6a3fae;
    --gold: #d6ad45;
    --gold-dark: #9c7a24;
    --navy: #1c1f4a;
  }
  * { box-sizing: border-box; margin: 0; padding: 0; }
  html, body { width: 1200px; height: 1000px; overflow: hidden; }
  body {
    background: var(--backdrop);
    font-family: "Open Sans", sans-serif;
    position: relative;
  }
  .card {
    position: absolute;
    left: 265px;
    width: 665px;
    height: 397px;
    background: var(--card);
    overflow: hidden;
    box-shadow: 0 4px 14px rgba(0,0,0,0.25);
  }
  .card-front { top: 73px; }
  .card-back { top: 533px; }

  .brand { position: absolute; }
  .brand-name {
    font-weight: 400;
    color: var(--text-light);
    white-space: nowrap;
    line-height: 1;
  }
  .brand-tagline {
    font-size: 9px;
    letter-spacing: 0.62em;
    color: var(--text-mid);
    text-transform: uppercase;
    white-space: nowrap;
    margin-top: 8px;
  }
  .brand-dot {
    position: absolute;
    border-radius: 50%;
    background: var(--blue);
  }

  .card-front .brand { left: 32px; top: 58px; padding-left: 52px; }
  .card-front .brand-dot { left: 0; top: 2px; width: 38px; height: 38px; }
  .card-front .brand-name { font-size: 29px; }

  .contact-block { position: absolute; left: 115px; top: 157px; }
  .person-name { font-size: 20px; font-weight: 600; color: var(--green); line-height: 1.2; }
  .person-role { font-size: 16px; color: var(--text-mid); margin-top: 2px; }
  .contact-list { list-style: none; margin-top: 16px; }
  .contact-list li {
    display: flex; align-items: center; gap: 8px;
    font-size: 16px; color: var(--text-light);
    height: 24.5px;
  }
  .contact-list li.social-first { margin-top: 6px; }
  .contact-list svg { width: 16px; height: 16px; flex: none; }

  .service-list { list-style: none; position: absolute; right: 0; top: 0; width: 260px; height: 100%; }
  .service {
    position: absolute; right: 34px;
    font-size: 16px; text-align: right; line-height: 1.25;
    transform: translateY(-50%);
  }
  .service::after {
    content: ""; position: absolute;
    right: -50px; top: 50%; transform: translateY(-50%);
    width: 32px; height: 32px; border-radius: 50%;
    background: currentColor;
  }
  .service-landscaping { top: 64px; color: var(--green); }
  .service-tarnwell { top: 138px; color: var(--teal); }
  .service-cleaning { top: 207px; color: var(--blue); }
  .service-plumbing { top: 276px; color: var(--purple); }
  .service-remodeling { top: 343px; color: var(--teal); }

  .seal { position: absolute; left: 423px; top: 170px; width: 110px; height: 110px; }

  .card-back .brand { right: 32px; top: 300px; text-align: right; }
  .card-back .brand-name { font-size: 32px; }
  .card-back .brand-dot { left: -56px; top: 0; width: 36px; height: 36px; background: var(--green); }
</style>
</head>
<body>

<section class="card card-front" aria-label="Business card front">
  <div class="brand">
    <span class="brand-dot"></span>
    <div class="brand-name">Kestrel Arc Services</div>
    <div class="brand-tagline">Fair work, fair price</div>
  </div>

  <div class="contact-block">
    <div class="person-name">Dorian Maltby</div>
    <div class="person-role">Creative Director</div>
    <ul class="contact-list">
      <li>
        <svg viewBox="0 0 16 16" aria-hidden="true"><path fill="#7dc35b" d="M2 6c0-2 2-3 6-3s6 1 6 3v1h-3V5.5H5V7H2zM4 8h8l1 5H3z"/><circle cx="8" cy="10.5" r="1.4" fill="#252525"/></svg>
        1-888-517-4KAS
      </li>
      <li>
        <svg viewBox="0 0 16 16" aria-hidden="true"><rect x="1" y="3.5" width="14" height="9" fill="#7dc35b"/><path d="M1.5 4l6.5 5 6.5-5" fill="none" stroke="#252525" stroke-width="1.3"/></svg>
        info@kestrelarcservices.example
      </li>
      <li>
        <svg viewBox="0 0 16 16" aria-hidden="true"><circle cx="8" cy="8" r="6.5" fill="none" stroke="#7dc35b" stroke-width="1.6"/><path d="M1.5 8h13M8 1.5c-3 3-3 10 0 13M8 1.5c3 3 3 10 0 13" fill="none" stroke="#7dc35b" stroke-width="1.2"/></svg>
        www.kestrelarcservices.example
      </li>
      <li class="social-first">
        <svg viewBox="0 0 16 16" aria-hidden="true"><circle cx="8" cy="8" r="7.5" fill="#7dc35b"/></svg>
        kestrelarc services
      </li>
      <li>
        <svg viewBox="0 0 16 16" aria-hidden="true"><circle cx="8" cy="8" r="7.5" fill="#7dc35b"/></svg>
        @kestrelarc services
      </li>
    </ul>
  </div>

  <ul class="service-list">
    <li class="service service-landscaping">Landscaping<br>Construction</li>
    <li class="service service-tarnwell">Tarnwell</li>
    <li class="service service-cleaning">Cleaning</li>
    <li class="service service-plumbing">Plumbing</li>
    <li class="service service-remodeling">Remodeling</li>
  </ul>
</section>

<section class="card card-back" aria-label="Business card back">
  <svg class="seal" viewBox="0 0 110 110" role="img" aria-label="Settle On The Sum That Feels Fair seal">
    <circle cx="55" cy="55" r="54" fill="var(--gold)"/>
    <circle cx="55" cy="55" r="46" fill="var(--gold-dark)"/>
    <circle cx="55" cy="55" r="43" fill="var(--navy)"/>
  </svg>

  <div class="brand">
    <span class="brand-dot"></span>
    <div class="brand-name">Kestrel Arc Services</div>
    <div class="brand-tagline">Fair work, fair price</div>
  </div>
</section>

</body>
</html>
```